Town Planning Consultants require lstationary design

Require a design to be used for our letterhead and report cover page. We have an approved logo.
we have attached our logo, and our temporary letterhead/cover page (SEE Cover) which we currently adapt for both purposes in the interim pending a permanent design. I have also attached an example (example report cover) of a report cover page that I like. perhaps similar with our colour scheme

Target Market(s)

?

Industry/Entity Type

Town

Colors
249fd4
3176b5

Requirements
Must have
• colours to match logo
• the text content in existing letterhead

```html
<!DOCTYPE html>
<html lang="en">
<head>
<meta charset="utf-8">
<title>Kestrel Planning Letterhead</title>
<link href="https://fonts.googleapis.com/css2?family=Questrial&family=Open+Sans:wght@600&display=swap" rel="stylesheet">
<style>
  :root {
    --backdrop: #d4d4d6;
    --paper: #f7f7f7;
    --ink: #2a2a2a;
    --muted: #7a7a7a;
    --brand-blue: #249fd4;
    --brand-deep: #3176b5;
    --band-grey: #9a9a9a;
    --sign-tint: #e4e8f3;
  }
  html, body {
    margin: 0; padding: 0;
    width: 1200px; height: 991px;
    overflow: hidden;
    background: var(--backdrop);
  }
  .letterhead {
    position: absolute;
    left: 267px; top: 25px;
    width: 666px; height: 940px;
    background: var(--paper);
    box-shadow: 0 2px 10px rgba(0,0,0,0.12);
    font-family: "Questrial", sans-serif;
    color: var(--ink);
    overflow: hidden;
  }
  .brand {
    position: absolute; left: 54px; top: 92px;
    display: flex; align-items: center; gap: 8px;
  }
  .brand-square { width: 14px; height: 14px; background: var(--brand-blue); }
  .brand-name {
    font-family: "Questrial", sans-serif;
    font-size: 34px; color: var(--brand-blue); line-height: 1;
  }
  .services {
    position: absolute; right: 53px; top: 62px;
    margin: 0; padding: 0; list-style: none;
    font-family: "Open Sans", sans-serif; font-weight: 600;
    font-size: 10.5px; color: var(--muted);
    text-align: right; line-height: 19px; letter-spacing: 0.2px;
  }
  .services li::after {
    content: ""; display: inline-block;
    width: 4px; height: 4px; border-radius: 50%;
    background: var(--brand-blue);
    margin-left: 6px; vertical-align: middle;
  }
  .date, .recipient, .salutation, .body-copy, .closing {
    position: absolute; left: 54px; font-size: 10px; line-height: 12px;
  }
  .date { top: 218px; }
  .recipient { top: 242px; }
  .salutation { top: 344px; font-weight: 700; }
  .body-copy { top: 372px; width: 559px; }
  .body-copy p { margin: 0 0 12px; text-align: justify; }
  .closing { top: 631px; }
  .closing strong { display: block; }
  .signature {
    position: absolute; left: 136px; top: 610px;
    width: 142px; height: 70px;
    background: var(--sign-tint);
  }
  .footer-address, .footer-contact {
    position: absolute; top: 865px;
    font-size: 8.5px; line-height: 12px; color: var(--ink);
  }
  .footer-address { left: 54px; }
  .footer-contact { left: 146px; }
  .footer-contact b { color: var(--brand-blue); font-weight: 700; }
  .footer-band { position: absolute; left: 0; bottom: 0; width: 666px; height: 60px; }
</style>
</head>
<body>
  <main class="letterhead">
    <div class="brand">
      <span class="brand-square"></span>
      <span class="brand-name">Kestrel Planning</span>
    </div>

    <ul class="services">
      <li>PLANNING</li>
      <li>DEVELOPMENT</li>
      <li>URBAN DESIGN</li>
      <li>CONSULTANTS</li>
    </ul>

    <div class="date">30.09.2015</div>
    <div class="recipient">Recipient's name<br>Lindenweg 14<br>10115 Berlin<br>Germany</div>

    <div class="salutation">Dear sir,</div>

    <div class="body-copy">
      <p>Communication is a very integral part of living creatures, animals and humans. Communication may be verbal or written. Written communication however is only applicable to human beings. Can you even imagine a world without communication? Verbal communication can be through telephones, webcams or in person. Written communication is through letters, emails and mobile phone messages.</p>
      <p>In today's world of great inventions and technology, letters have somehow become redundant. It is the time for text messages or chats. But they still can communicate a lot more than all other modes of communication. Organizations and various government departments still bank on letters as a strong medium of communication. There is no comparison in costs of sending letters as compared to costs of mobile phone messages though – letters are far cheaper. Letters now commonly known as "hard copy documents" are considered more relevant and important than email copies of text messages as proof or evidence of some sort.</p>
      <p>Letters speak volumes about a person or an organization that writes it. So one must take utmost care ensuring that the language used in any letter is appropriate for the occasion for which it is being written. Since a letter is also a written proof or document, if there are certain things that should not form a part of it, then that too should be carefully handled.</p>
      <p>Writing a good letter is an art. But if for some reason someone is unable to write that perfect letter, these different types of letters provide a base for you to build on. Sample letters have been given for everyone to understand what all information needs to form a part of the letter type and then it can be customized.</p>
    </div>

    <div class="closing">Yours Sincerely,<strong>Elin Marsh</strong></div>
    <div class="signature" role="img" aria-label="Handwritten signature of the sender"></div>

    <div class="footer-address">12 Harbour Ridge Road<br>CLAREMONT<br>NSW 2480</div>
    <div class="footer-contact">
      <b>T:</b> +61 (2) 5550 1234<br>
      <b>M:</b> +61 (0) 400 555 018<br>
      <b>E:</b> hello@kestrelplanning.com.au
    </div>

    <svg class="footer-band" viewBox="0 0 666 60" preserveAspectRatio="none">
      <polygon points="0,25 0,60 280,60" fill="var(--brand-blue)"/>
      <polygon points="194,60 666,4 666,60" fill="var(--band-grey)"/>
    </svg>
  </main>
</body>
</html>
```